Design Business Card based on company's details and VFX guidelines (refer to page 16). use VFX logo in color that best suites overall design.

Bellmoor Ledger & Returns Pty Ltd
Principal: Mrs Helena Quorvine
Address: Suite 5.12 247 Penwick Street, Alexandria NSW 2015
Postal: PO Box 7419
ALEXANDRIA NSW 2015
Land line: 02 91572368
Mobile: 0417 562 308
email: helena@bellmoorledger.com.au
web: www.bellmoorledger.com.au

```html
<!DOCTYPE html>
<html lang="en">
<head>
<meta charset="utf-8">
<title>Bellmoor Ledger &amp; Returns — Business Card</title>
<link rel="stylesheet" href="https://fonts.googleapis.com/css2?family=Michroma&family=Arimo:wght@400;700&display=swap">
<style>
  :root {
    --stage: #2b2b2b;
    --card: #f4f4f4;
    --card-shade: #e2e2e2;
    --brand-red: #8e1b20;
    --brand-red-deep: #6e1216;
    --brand-grey: #6d6e70;
    --rule-grey: #9a9a9a;
    --badge-blue: #2f78c4;
    --on-red: #ffffff;
  }
  * { box-sizing: border-box; margin: 0; padding: 0; }
  html, body { width: 1200px; height: 997px; overflow: hidden; }
  body {
    background: var(--stage);
    font-family: "Arimo", Arial, sans-serif;
    position: relative;
  }
  .card {
    position: absolute;
    width: 600px;
    height: 340px;
    left: 300px;
    border-radius: 16px;
    overflow: hidden;
    background: linear-gradient(160deg, #ffffff 0%, var(--card) 55%, var(--card-shade) 100%);
    box-shadow: 0 14px 30px rgba(0,0,0,.45);
  }
  .card--front { top: 100px; }
  .card--back  { top: 540px; }

  /* wordmark */
  .wordmark { position: absolute; text-align: center; }
  .wordmark__name {
    font-family: "Michroma", "Arimo", sans-serif;
    color: var(--brand-red);
    letter-spacing: 1px;
    white-space: nowrap;
    line-height: 1.2;
  }
  .wordmark__sub {
    font-family: "Michroma", "Arimo", sans-serif;
    color: var(--brand-grey);
    letter-spacing: 7px;
    white-space: nowrap;
    line-height: 1.2;
  }
  .wordmark__rule { height: 1px; background: var(--rule-grey); margin-left: auto; margin-right: auto; }

  /* brand name stand-in mark */
  .brand-mark {
    position: absolute;
    border-radius: 50%;
    border: 6px solid var(--brand-grey);
    display: flex;
    align-items: center;
    justify-content: center;
    font-family: "Arimo", Arial, sans-serif;
    font-weight: 700;
    color: var(--brand-red);
    letter-spacing: 1px;
  }

  /* front card */
  .card--front .brand-mark { width: 124px; height: 124px; left: 110px; top: 24px; font-size: 17px; }
  .card--front .wordmark { left: 40px; top: 162px; width: 440px; }
  .card--front .wordmark__name { font-size: 25px; }
  .card--front .wordmark__sub { font-size: 11px; margin-top: 4px; }
  .card--front .wordmark__rule { margin-top: 8px; width: 400px; }
  .web-band {
    position: absolute; left: 0; right: 0; bottom: 40px; height: 36px;
    background: linear-gradient(180deg, var(--brand-red) 0%, var(--brand-red-deep) 100%);
    color: var(--on-red);
    font-size: 16px;
    display: flex; align-items: center; justify-content: flex-end;
    padding-right: 120px;
    letter-spacing: .3px;
  }
  .partner-badge {
    position: absolute; right: 30px; bottom: 82px;
    width: 70px; height: 28px;
    border: 2px solid var(--badge-blue);
    background: #ffffff;
  }
  .partner-badge::before {
    content: ""; position: absolute; left: 0; top: 0; bottom: 0; width: 44px;
    background: var(--badge-blue);
  }

  /* back card */
  .back-art { position: absolute; inset: 0; }
  .card--back .wordmark { right: 40px; top: 40px; width: 420px; }
  .card--back .wordmark__name { font-size: 25px; }
  .card--back .wordmark__sub { font-size: 12px; margin-top: 3px; }
  .card--back .wordmark__rule { margin-top: 8px; width: 300px; margin-left: 0; }
  .card--back .brand-mark {
    width: 130px; height: 130px; left: 60px; top: 180px; font-size: 18px;
    background: var(--card);
  }
  .contact {
    position: absolute; right: 26px; top: 150px;
    color: var(--on-red); text-align: right;
    font-size: 13px; line-height: 1.55;
  }
  .contact__name { font-weight: 700; font-size: 15px; letter-spacing: .5px; }
  .contact__role { margin-bottom: 10px; font-size: 14px; }
  .contact__line { display: flex; justify-content: flex-end; align-items: center; gap: 8px; }
  .contact__line svg { width: 11px; height: 11px; flex: none; }
</style>
</head>
<body>

<section class="card card--front" aria-label="Business card front">
  <div class="brand-mark">BELLMOOR</div>
  <div class="wordmark">
    <div class="wordmark__name">BELLMOOR LEDGER</div>
    <div class="wordmark__sub">&amp; RETURNS</div>
    <div class="wordmark__rule"></div>
  </div>
  <div class="partner-badge" role="img" aria-label="Professional body badge"></div>
  <div class="web-band">www.bellmoorledger.com.au</div>
</section>

<section class="card card--back" aria-label="Business card back">
  <svg class="back-art" viewBox="0 0 600 340" preserveAspectRatio="none" aria-hidden="true">
    <defs>
      <linearGradient id="redFill" x1="0" y1="0" x2="0" y2="1">
        <stop offset="0" stop-color="#9a1f25"/>
        <stop offset="1" stop-color="#6a1115"/>
      </linearGradient>
    </defs>
    <path d="M0,235 C170,262 360,128 600,118 L600,340 L0,340 Z" fill="url(#redFill)"/>
    <path d="M0,205 C170,232 360,92 600,92 L600,106 C360,112 170,252 0,226 Z" fill="#6d6e70"/>
  </svg>

  <div class="wordmark">
    <div class="wordmark__name">BELLMOOR LEDGER</div>
    <div class="wordmark__sub">&amp; RETURNS</div>
    <div class="wordmark__rule"></div>
  </div>

  <div class="brand-mark">BELLMOOR</div>

  <div class="contact">
    <div class="contact__name">MRS HELENA QUORVINE</div>
    <div class="contact__role">Principal</div>
    <div class="contact__line">02 91572368
      <svg viewBox="0 0 12 12"><path d="M2 1h3l1 3-2 1a6 6 0 0 0 3 3l1-2 3 1v3c-6 0-10-4-10-9z" fill="#fff"/></svg>
    </div>
    <div class="contact__line">Mobile: 0417 562 308
      <svg viewBox="0 0 12 12"><rect x="3" y="0.5" width="6" height="11" rx="1" fill="none" stroke="#fff"/><circle cx="6" cy="9.5" r=".8" fill="#fff"/></svg>
    </div>
    <div class="contact__line">email: helena@bellmoorledger.com.au
      <svg viewBox="0 0 12 12"><rect x=".5" y="2.5" width="11" height="7" fill="#fff"/><path d="M.5 2.5 6 7l5.5-4.5" fill="none" stroke="#8e1b20"/></svg>
    </div>
    <div class="contact__line">Suite 5.12 247 Penwick Street, Alexandria NSW 2015
      <svg viewBox="0 0 12 12"><path d="M6 11S2 7 2 4.5a4 4 0 0 1 8 0C10 7 6 11 6 11z" fill="#fff"/><circle cx="6" cy="4.5" r="1.4" fill="#8e1b20"/></svg>
    </div>
  </div>
</section>

</body>
</html>
```